Website for Ledger Prowl a cyrpto Mining company that sells crypto mining rigs

β€œIn the age of de-centralised financial services, individuals with a relatively small investment can use their own hardware to process crypto transactions and earn a substantial second income.”

Ledger Prowl provide a personal home and hosted mining solutions to enable individuals to earn monthly crypto currencies of today and the future.”
Home/Products/About
Images – I had assumed this was part of the Design? For the home page I have a 10 second video of blockchain. I can only find on Framevault For any text or sections please refer to our old website www.thirdotter.ae
https://www.framevault.example/video/clip-2741905316-block-chain-concept---consists-network-connections I can buy and send?
On each page I will have a video similar, can you just put placeholder images and videos. I can replace. I am pretty good with Wordpress.
Updates

Please use text from my old website www.thirdottermining.example

Target Market(s)

High Net wealth interested in Crypto

Industry/Entity Type

Crypto Mining

Coding

Coded - Design and coding required

Number of Pages Required

5+ page

Font styles to use
Other font styles liked:
• Sansation

Colors
0054AA
0677BA
7BADD7
CADEEF
E8F1F8

Requirements
Must have
• Video as banner (Will supply Video), Wordpress
Nice to have
• Will need Member login and Shop in future, please ensure this will be possible. (But not part of this project)

```html
<!DOCTYPE html>
<html lang="en">
<head>
<meta charset="utf-8">
<title>About – Ledger Prowl</title>
<link rel="stylesheet" href="https://fonts.googleapis.com/css2?family=Montserrat:wght@400;500;600;700&family=Oswald:wght@500&display=swap">
<style>
:root{
  --blue-deep:#0054AA;
  --blue:#0677BA;
  --blue-bright:#1E9BE8;
  --blue-soft:#7BADD7;
  --blue-pale:#CADEEF;
  --blue-mist:#E8F1F8;
  --ink:#1B1F26;
  --muted:#4A5563;
  --night:#0B1620;
  --footer:#121417;
  --white:#FFFFFF;
}
*{margin:0;padding:0;box-sizing:border-box}
html,body{width:716px;height:1200px;overflow:hidden;background:var(--white)}
body{position:relative;font-family:"Montserrat",Arial,sans-serif;color:var(--ink)}
.page{position:absolute;inset:0;background:linear-gradient(180deg,var(--blue-mist) 0%,#F6FAFD 60%,var(--white) 100%)}
.hero-media{position:absolute;left:0;top:0;width:716px;height:420px;
  background:radial-gradient(ellipse at 50% 55%,#1B4C66 0%,#0F2B3D 40%,var(--night) 80%);
  clip-path:polygon(0 0,100% 0,100% 62%,0 100%)}
.contact-band{position:absolute;left:0;top:700px;width:716px;height:360px;background:var(--blue-pale);opacity:.45;
  clip-path:polygon(0 35%,100% 0,100% 70%,0 100%)}
.nav{position:absolute;left:0;top:0;width:716px;height:64px}
.brand{position:absolute;left:74px;top:22px;display:flex;align-items:center;gap:8px;font-weight:600;font-size:15px;color:var(--blue-bright);letter-spacing:.04em}
.brand-dot{width:20px;height:20px;border-radius:50%;background:var(--blue-bright)}
.menu{position:absolute;left:290px;top:27px;display:flex;gap:34px;font-size:9px;color:var(--white);list-style:none}
.menu .active{color:var(--blue-bright)}
.login{position:absolute;left:560px;top:25px;display:flex;align-items:center;gap:6px;font-size:8px;font-weight:700;color:var(--white);letter-spacing:.05em}
.cart{position:absolute;left:616px;top:17px;width:30px;height:30px;border-radius:50%;background:var(--blue-bright);display:flex;align-items:center;justify-content:center}
.page-title{position:absolute;left:0;width:716px;top:92px;text-align:center;font-family:"Oswald",Arial,sans-serif;font-weight:500;font-size:30px;letter-spacing:.4em;color:var(--white);padding-left:.4em}
.intro{position:absolute;left:74px;top:250px;width:568px;height:165px;background:linear-gradient(160deg,var(--blue) 0%,var(--blue-deep) 100%);color:var(--white);text-align:center;padding:30px 56px}
.intro-lead{font-size:9px;font-weight:600;margin-bottom:12px}
.intro-body{font-size:8.6px;line-height:1.6}
.team-card{position:absolute;top:460px;width:230px}
.team-card.first{left:74px}.team-card.second{left:412px}
.team-photo{width:230px;height:200px;background:linear-gradient(135deg,#C9CFD4,#8C939A 55%,#E4E6E8)}
.team-card.second .team-photo{background:linear-gradient(135deg,#F3F4F5,#C7B4A8 50%,#E9ECEE)}
.team-name{margin-top:16px;font-size:13px;font-weight:700}
.team-role{margin-top:8px;font-size:8px;line-height:1.55;color:var(--muted)}
.contact{position:absolute;left:74px;top:770px;width:568px;height:280px;background:linear-gradient(170deg,var(--blue) 0%,var(--blue-deep) 100%);color:var(--white)}
.contact-title{position:absolute;left:48px;top:38px;font-family:"Oswald",Arial,sans-serif;font-weight:500;font-size:17px;letter-spacing:.32em}
.contact-text{position:absolute;left:48px;top:76px;width:150px;font-size:8px;line-height:1.6}
.contact-line{position:absolute;left:48px;display:flex;align-items:center;gap:12px;font-size:8px;font-weight:600}
.contact-line.mail{top:152px}.contact-line.phone{top:192px}
.icon-disc{width:30px;height:30px;border-radius:50%;background:var(--blue-bright);display:flex;align-items:center;justify-content:center}
.form{position:absolute;left:278px;top:36px;width:242px}
.field{height:24px;background:var(--white);border:1px solid var(--blue-pale);font-size:7px;color:#9AA4AF;padding:7px 8px}
.field.message{height:126px;position:relative}
.send{position:absolute;right:8px;bottom:8px}
.footer{position:absolute;left:0;top:1080px;width:716px;height:120px;background:linear-gradient(180deg,#1A1D21,var(--footer));color:#C4C9CF;text-align:center}
.footer .brand{position:static;justify-content:center;margin-top:24px}
.footer-copy{margin-top:14px;font-size:7.5px;line-height:1.7}
.chat{position:absolute;right:28px;bottom:16px}
</style>
</head>
<body>
<main class="page">
  <div class="hero-media" role="img" aria-label="Dark blockchain banner video placeholder with glowing circuitry"></div>
  <div class="contact-band"></div>

  <header class="nav">
    <div class="brand"><span class="brand-dot"></span>Ledger Prowl</div>
    <ul class="menu"><li>Home</li><li class="active">About</li><li>Products</li></ul>
    <div class="login">
      <svg width="11" height="11" viewBox="0 0 12 12" fill="none" stroke="#1E9BE8" stroke-width="1.2"><circle cx="6" cy="4" r="2.5"/><path d="M1.5 11.5c0-2.5 2-4 4.5-4s4.5 1.5 4.5 4"/></svg>LOGIN
    </div>
    <div class="cart"><svg width="12" height="12" viewBox="0 0 12 12" fill="none" stroke="#fff" stroke-width="1.2"><path d="M2 4h8l-1 7H3z"/><path d="M4 4a2 2 0 0 1 4 0"/></svg></div>
  </header>

  <h1 class="page-title">ABOUT</h1>

  <section class="intro">
    <p class="intro-lead">IT and Operations since 2000, Digital Payments since 2007, Crypto since 2012.</p>
    <p class="intro-body">Dimitar and Oleg were part of the core team that built Paynorth.com. Reid has been running IT and Operation teams of large companies for many years before setting up his own IT and Security Consultancy. Together this team knew how to build, run and scale technology in Crypto and Payments, we only make 10% of your profits so we're dedicated to make your Third Otter mining rigs perform.</p>
  </section>

  <article class="team-card first">
    <div class="team-photo" role="img" aria-label="Photo of the technology and operations team at work"></div>
    <h2 class="team-name">Dimitar &amp; Oleg</h2>
    <p class="team-role">Our Technology and Operations gurus who track the crypto markets daily. Their remote access to the Third Otter mining rigs ensure they are optimised.</p>
  </article>
  <article class="team-card second">
    <div class="team-photo" role="img" aria-label="Portrait photo of the co-founder"></div>
    <h2 class="team-name">Reid Callander</h2>
    <p class="team-role">Co-Founder who designs, builds and maintains our hardware and software solutions.</p>
  </article>

  <section class="contact">
    <h2 class="contact-title">GET IN TOUCH</h2>
    <p class="contact-text">If you're here it means you want to start a journey. We would love to get to know you and take you on that journey. We'll be perfect for each other – you'll see...</p>
    <div class="contact-line mail"><span class="icon-disc"><svg width="12" height="10" viewBox="0 0 12 10" fill="#fff"><path d="M0 0h12v10H0z"/><path d="M0 0l6 5 6-5" fill="none" stroke="#1E9BE8" stroke-width="1.2"/></svg></span>reid@ledgerprowl.ae</div>
    <div class="contact-line phone"><span class="icon-disc"><svg width="12" height="12" viewBox="0 0 12 12" fill="#fff"><path d="M2.5 0.5l2 2.5-1.2 1.5c.7 1.6 2 2.9 3.7 3.7L8.5 7l2.8 2-1.2 2.5C5 11 1 7 .5 2z"/></svg></span>+971 50 214 3378</div>
    <form class="form">
      <div class="field">Name</div>
      <div class="field">Email</div>
      <div class="field">Subject</div>
      <div class="field message">Type your message...
        <svg class="send" width="12" height="11" viewBox="0 0 12 11" fill="#1E9BE8"><path d="M0 5L12 0 9 11 6 7z"/></svg>
      </div>
    </form>
  </section>

  <footer class="footer">
    <div class="brand"><span class="brand-dot"></span>Ledger Prowl</div>
    <p class="footer-copy">©2021 by Third Otter Mining.<br>A Prowl Solutions LLC Company, business license number 2418873,<br>registered with Harbour Free Zone.</p>
    <svg class="chat" width="22" height="20" viewBox="0 0 22 20" fill="none" stroke="#fff" stroke-width="1.4"><path d="M3 2h14a2 2 0 0 1 2 2v8a2 2 0 0 1-2 2H8l-5 4v-4a2 2 0 0 1-2-2V4a2 2 0 0 1 2-2z"/><path d="M6 7h8M6 10h6"/></svg>
  </footer>
</main>
</body>
</html>
```